New header and menu

Problems to be solved.
a) Screen resolution: Our current menu and header doesn't use the space optimally. Visitors with 1358 resolution don't see a lot of the content on the page which kills conversion. So we need a smaller header and menu. Menu and top sticky bars are very big
b) Call to actions: We need our menu to be more efficient and provide clear call to actions to the visitor (contact us, looking for jobs and get a free quote being most important).
c) mobile: On mobile our current menu is more or less useless.

What we need!
We need a menu and header that maximizes conversion and optimizes space usage for all resultions and devices.

You can check on our website: http://www.briskwillow.com

```html
<!DOCTYPE html>
<html lang="en">
<head>
<meta charset="utf-8">
<title>Brisk Willow – Header and Menu</title>
<link href="https://fonts.googleapis.com/css2?family=Roboto:wght@300;400;500;700&display=swap" rel="stylesheet">
<style>
:root{
  --cyan-light:#74f3fd;
  --cyan:#4cc3ef;
  --yellow:#f2c200;
  --ink:#0a0b0c;
  --grey:#8f969b;
  --white:#ffffff;
}
*{margin:0;padding:0;box-sizing:border-box}
html,body{width:819px;height:1200px;overflow:hidden;background:var(--white);font-family:"Roboto",Helvetica,Arial,sans-serif}
.canvas{position:relative;width:819px;height:1200px}
.abs{position:absolute}
.topbar{left:0;top:0;width:819px;height:18px;background:var(--cyan-light)}
.social{top:3px;width:12px;height:12px;border-radius:50%;background:var(--white)}
.top-search{left:750px;top:0;width:20px;height:18px;border-left:1px solid var(--white)}
.lang{left:771px;top:0;width:48px;height:18px;background:var(--cyan);color:var(--white);font-size:8px;letter-spacing:.5px;line-height:18px;text-align:center}
.brand-mark{width:34px;height:34px;border-radius:50%;background:var(--cyan-light)}
.brand-name{font-weight:300;color:var(--cyan);white-space:nowrap}
.tagline{color:var(--grey);font-weight:300;white-space:nowrap}
.nav-item{top:53px;font-size:11px;color:var(--grey);transform:translateX(-50%)}
.nav-active{left:266px;top:50px;width:150px;height:20px;background:var(--cyan);color:var(--white);font-size:11px;line-height:20px;padding-left:5px}
.nav-active svg{position:absolute;right:4px;top:6px}
.hero{left:0;top:198px;width:819px;height:259px;background:var(--ink);z-index:1}
.dropdown{left:266px;top:79px;width:264px;height:157px;background:var(--cyan);border-radius:2px;z-index:2}
.drop-link{font-size:7.3px;color:var(--white);white-space:nowrap;z-index:3}
.cta{left:0;width:199px;height:25px;color:var(--white);font-size:10px;font-weight:700;letter-spacing:1px;line-height:25px;padding-left:33px}
.cta-quote{top:87px;background:var(--cyan)}
.cta-job{top:116px;background:var(--yellow)}
.contact-line{left:56px;font-size:9.5px;color:var(--grey);letter-spacing:.4px}
.m-lang{left:264px;top:555px;width:305px;height:19px;background:var(--cyan-light);color:var(--white);font-size:8px;letter-spacing:.5px;line-height:19px;text-align:center}
.m-menu{left:316px;top:641px;width:201px;height:113px;background:var(--cyan-light)}
.m-first{left:316px;top:641px;width:201px;height:24px;background:var(--cyan)}
.m-item{left:326px;font-size:10.5px;color:var(--white);font-weight:300}
.m-arrow{left:491px}
.m-job{left:316px;top:765px;width:201px;height:25px;background:var(--yellow);font-size:10px;font-weight:700;text-align:center;line-height:25px;color:var(--ink)}
.m-content{left:273px;top:798px;width:288px;height:141px;background:var(--ink);color:var(--white);font-size:10px;text-align:center;line-height:141px;letter-spacing:.3px}
</style>
</head>
<body>
<div class="canvas">
  <!-- top utility bar -->
  <div class="abs topbar"></div>
  <span class="abs social" style="left:680px"></span>
  <span class="abs social" style="left:698px"></span>
  <span class="abs social" style="left:716px"></span>
  <div class="abs top-search">
    <svg width="20" height="18" viewBox="0 0 20 18"><circle cx="9" cy="8" r="3" fill="none" stroke="#fff" stroke-width="1.4"/><line x1="11" y1="10" x2="13.5" y2="12.5" stroke="#fff" stroke-width="1.6"/></svg>
  </div>
  <div class="abs lang">ENGLISH</div>

  <!-- brand -->
  <span class="abs brand-mark" style="left:28px;top:28px"></span>
  <div class="abs brand-name" style="left:78px;top:38px;font-size:19px">BRISKWILLOW</div>
  <div class="abs tagline" style="left:81px;top:60px;font-size:8.5px">Your content &amp; translation agency</div>

  <!-- main navigation -->
  <div class="abs nav-active">TRANSLATION SERVICES
    <svg width="8" height="7" viewBox="0 0 8 7"><path d="M0 0H8L4 7Z" fill="#fff"/></svg>
  </div>
  <div class="abs nav-item" style="left:476px">PRICES</div>
  <div class="abs nav-item" style="left:569px">CONTENT</div>
  <div class="abs nav-item" style="left:653px">BLOG</div>
  <div class="abs nav-item" style="left:739px">ABOUT</div>

  <!-- calls to action -->
  <div class="abs cta cta-quote">GET YOUR FREE QUOTE !</div>
  <div class="abs cta cta-job">LOOKING FOR A JOB?</div>
  <svg class="abs" style="left:35px;top:149px" width="14" height="14" viewBox="0 0 14 14"><path d="M3 1l3 3-1.5 2c1 2 2 3 3.5 3.5L10 8l3 3-2 2C6 13 1 8 1 3z" fill="#9aa1a6"/></svg>
  <div class="abs contact-line" style="top:150px;font-weight:500">020-8400 1275</div>
  <svg class="abs" style="left:37px;top:174px" width="14" height="9" viewBox="0 0 14 9"><rect x="0.5" y="0.5" width="13" height="8" fill="#9aa1a6"/><path d="M0.5 0.5L7 5L13.5 0.5" fill="none" stroke="#fff" stroke-width="1"/></svg>
  <div class="abs contact-line" style="top:173px;font-weight:300">CONTACT US</div>

  <!-- page content area -->
  <div class="abs hero"></div>

  <!-- translation services dropdown, above the content area -->
  <div class="abs dropdown"></div>
  <div class="abs drop-link" style="left:282px;top:88px">INTERPRATATION SERVICES</div>
  <div class="abs drop-link" style="left:411px;top:88px">BULK SEO TRANSLATION</div>
  <div class="abs drop-link" style="left:282px;top:111px">CONTENT TRANSLATION</div>
  <div class="abs drop-link" style="left:411px;top:111px">DANISH TRANSLATION</div>
  <div class="abs drop-link" style="left:282px;top:134px">ENGLISH TRANSLATION</div>
  <div class="abs drop-link" style="left:411px;top:134px">FINNISH TRANSLATION</div>
  <div class="abs drop-link" style="left:282px;top:159px">FRENCH TRANSLATION</div>
  <div class="abs drop-link" style="left:410px;top:158px">JAPANESE TRANSLATION</div>
  <div class="abs drop-link" style="left:282px;top:183px">NORWEGIAN TRANSLATION</div>
  <div class="abs drop-link" style="left:410px;top:184px">SWEDISH TRANSLATION</div>
  <div class="abs drop-link" style="left:282px;top:207px">TURKISH TRANSLATION</div>
  <div class="abs drop-link" style="left:478px;top:209px">MORE...</div>

  <!-- mobile header -->
  <div class="abs m-lang">ENGLISH
    <svg style="position:absolute;left:32px;top:6px" width="8" height="8" viewBox="0 0 8 8"><path d="M8 0V8L0 4Z" fill="#fff"/></svg>
    <svg style="position:absolute;right:32px;top:5px" width="8" height="8" viewBox="0 0 8 8"><path d="M0 0V8L8 4Z" fill="#fff"/></svg>
  </div>
  <span class="abs brand-mark" style="left:332px;top:591px"></span>
  <div class="abs brand-name" style="left:375px;top:598px;font-size:15px">BRISKWILLOW</div>
  <div class="abs tagline" style="left:377px;top:616px;font-size:7px">Your content &amp; translation agency</div>
  <svg class="abs" style="left:528px;top:599px" width="18" height="18" viewBox="0 0 18 18"><circle cx="7" cy="7" r="4.5" fill="none" stroke="#74f3fd" stroke-width="2.4"/><line x1="10.5" y1="10.5" x2="15" y2="15" stroke="#74f3fd" stroke-width="3"/></svg>

  <div class="abs m-menu"></div>
  <div class="abs m-first"></div>
  <div class="abs m-item" style="top:647px;font-weight:400">TRANSLATION SERVICES</div>
  <div class="abs m-item" style="top:670px">PRICES</div>
  <div class="abs m-item" style="top:691px">CONTACT</div>
  <div class="abs m-item" style="top:711px">BLOG</div>
  <div class="abs m-item" style="top:733px">ABOUT</div>
  <svg class="abs m-arrow" style="top:649px" width="9" height="8" viewBox="0 0 9 8"><path d="M0 0H9L4.5 8Z" fill="#fff"/></svg>
  <svg class="abs m-arrow" style="top:673px" width="9" height="8" viewBox="0 0 9 8"><path d="M0 0H9L4.5 8Z" fill="#fff"/></svg>
  <svg class="abs m-arrow" style="top:694px" width="9" height="8" viewBox="0 0 9 8"><path d="M0 0H9L4.5 8Z" fill="#fff"/></svg>
  <svg class="abs m-arrow" style="top:715px" width="9" height="8" viewBox="0 0 9 8"><path d="M0 0H9L4.5 8Z" fill="#fff"/></svg>
  <svg class="abs m-arrow" style="top:736px" width="9" height="8" viewBox="0 0 9 8"><path d="M0 0H9L4.5 8Z" fill="#fff"/></svg>

  <div class="abs m-job">LOOKING FOR A JOB?</div>
  <div class="abs m-content">CONTENT HERE</div>
</div>
</body>
</html>
```